NEW Escape Room. Fun, Dark and Mysterious.

Escape Room Website. Bookings and scheduling of appointments will be organised with Bolkit through the site. Most appointments will be created online through the booking system with some payments coming through in person by drop-ins. Groups will be from 2 - 8 people with a sliding scale of prices. We will start with one game playable and one saying coming soon. We will also eventually have 4 games up and running at once so will need it to be able to expand. We don't have any images of the rooms because it all relies heavily on mystery. Appointments are each 1 hour long with 30 minutes in between.

Target Market(s)

15-35 year olds

Coding

Coded - Design and coding required

Number of Pages Required

5+ page

Font styles to use
Decorative

Colors

Designer to choose colors to be used in the design.

Requirements
Must have
• Graphics showing what an escape room is.
• Page for About - What is an escape room
• Page for Games - Showing each of the different games which can be played with links to booking page. We have one game to start - the tailor's shadows. A victorian doctors office and serial killers. Then a game coming soon which is aztec/mayan/jungle/captain Worrel feel.
• FAQ Page
Nice to have
• Graphics for multiple players ie 2 players, 3 players, 4 players etc
• Dark and Mysterious feel.
• Inspiration from Cipher Vault, Lockwise Hall, Puzzle Harbor
Should not have
• Cartoony/childish. Pink.
• Not bloody or dripping letters etc - not cliche.
• Not horror themed.

```html
<!DOCTYPE html>
<html lang="en">
<head>
<meta charset="utf-8">
<title>Hollow Key – Escape Room</title>
<link href="https://fonts.googleapis.com/css2?family=Roboto+Slab:wght@500;700;800&family=Poppins:wght@500;600;700&family=Montserrat:wght@300;400&display=swap" rel="stylesheet">
<style>
:root{
  --black:#000;
  --coal:#111;
  --coal-2:#171717;
  --amber:#e8902a;
  --amber-soft:#d9a24a;
  --rust:#c96a2a;
  --rust-deep:#8a2b18;
  --brown:#2b1e14;
  --white:#fff;
  --grey:#cfcfcf;
  --grey-dim:#a9a9a9;
}
*{margin:0;padding:0;box-sizing:border-box}
html,body{width:1200px;height:2907px;overflow:hidden;background:var(--black)}
body{position:relative;font-family:"Montserrat",sans-serif;color:var(--white)}
.abs{position:absolute}
.center{left:0;width:1200px;text-align:center}

/* hero */
.hero-photo{left:0;top:0;width:1200px;height:841px;
  background:radial-gradient(ellipse at 50% 45%,#4a4a4a 0%,#2a2a2a 40%,#101010 80%)}
.hero-chevron{left:0;top:600px;width:1200px;height:245px}
.nav a{position:absolute;top:48px;font-family:"Poppins",sans-serif;font-weight:600;font-size:17px;color:var(--white);text-decoration:none;letter-spacing:.2px}
.nav a.active{color:var(--amber-soft)}
.nav .sep{position:absolute;top:50px;width:1px;height:22px;background:#bbb}
.brand{left:500px;top:60px;width:200px;text-align:center}
.brand .dot{width:54px;height:54px;border:2px solid var(--amber);border-radius:50%;margin:0 auto 10px}
.brand span{font-family:"Poppins",sans-serif;font-weight:700;font-size:22px;color:var(--amber);letter-spacing:1px}
.hero-kicker{top:288px;font-family:"Roboto Slab",serif;font-weight:700;font-size:43px;color:var(--amber)}
.hero-title{top:345px;font-family:"Roboto Slab",serif;font-weight:800;font-size:84px;line-height:1;color:var(--white)}
.btn-book{left:503px;top:457px;width:197px;height:57px;background:linear-gradient(180deg,#f0a03a,#d06a20);
  font-family:"Poppins",sans-serif;font-weight:600;font-size:18px;letter-spacing:1.5px;line-height:57px;text-align:center}
.arrow-l,.arrow-r{top:349px;width:36px;height:36px}
.arrow-l{left:68px}.arrow-r{left:1100px}

/* about */
.about-band{left:0;top:841px;width:1200px;height:540px;background:var(--coal)}
.about-hex{left:166px;top:852px;width:360px;height:412px}
.about-title{left:604px;top:875px;font-family:"Roboto Slab",serif;font-weight:700;font-size:35px}
.about-copy{left:607px;width:490px;font-weight:300;font-size:16.5px;line-height:25px;color:var(--grey)}
.btn-outline{border:2px solid var(--amber);color:var(--amber);font-family:"Poppins",sans-serif;font-weight:600;text-align:center;letter-spacing:.5px}
.btn-learn{left:615px;top:1166px;width:170px;height:49px;line-height:45px;font-size:14px}

/* who can play */
.play-band{left:0;top:1300px;width:1200px;height:460px}
.play-title{top:1400px;font-family:"Roboto Slab",serif;font-weight:700;font-size:30px}
.player{top:1490px;width:330px;height:100px}
.player svg{position:absolute;left:0;top:0}
.player h3{position:absolute;left:106px;top:18px;font-family:"Poppins",sans-serif;font-weight:600;font-size:20px;color:var(--amber);letter-spacing:.8px}
.player p{position:absolute;left:106px;top:48px;width:225px;font-weight:300;font-size:13px;line-height:21px;color:var(--grey)}

/* how it works */
.how-photo{left:0;top:1654px;width:1200px;height:642px;
  background:radial-gradient(ellipse at 50% 55%,#050505 0%,#1a1a1a 45%,#2d2d2d 100%)}
.how-chevron{left:0;top:1640px;width:1200px;height:125px}
.how-title{top:1806px;font-family:"Roboto Slab",serif;font-weight:700;font-size:29px;color:var(--amber)}
.how-copy{top:1856px;font-weight:300;font-size:16.5px;line-height:25px;color:var(--grey)}
.step{top:1953px;width:320px;text-align:center}
.step .ring{width:142px;height:142px;margin:0 auto}
.step h3{margin-top:18px;font-family:"Poppins",sans-serif;font-weight:600;font-size:20px;color:var(--amber)}
.step p{margin-top:6px;font-weight:300;font-size:13px;line-height:20px;color:var(--grey)}
.step-arrow{top:1995px;width:70px;height:50px}

/* booking */
.book-band{left:0;top:2295px;width:1200px;height:450px;background:linear-gradient(100deg,var(--rust) 0%,#b9532a 50%,var(--rust-deep) 100%)}
.book-title{top:2373px;font-family:"Roboto Slab",serif;font-weight:700;font-size:37px}
.book-copy{top:2433px;font-weight:400;font-size:16.5px;line-height:25px}
.btn-schedule{left:436px;top:2511px;width:349px;height:56px;border:2px solid var(--white);font-family:"Poppins",sans-serif;font-weight:600;font-size:16px;letter-spacing:1.5px;line-height:52px;text-align:center}
.foot-chevron{left:0;top:2640px;width:1200px;height:267px}
.foot-brand{left:520px;top:2620px;width:160px;text-align:center}
.foot-brand .dot{width:40px;height:40px;border:2px solid var(--amber);border-radius:50%;margin:0 auto 6px;background:var(--black)}
.foot-brand span{font-family:"Poppins",sans-serif;font-weight:700;font-size:17px;color:var(--amber)}

/* footer */
.foot-nav a{position:absolute;top:2763px;font-family:"Poppins",sans-serif;font-weight:600;font-size:17px;color:#bdbdbd;text-decoration:none;transform:translateX(-50%)}
.copyright{top:2800px;font-size:13px;color:#bdbdbd}
.social{top:2836px;width:33px;height:33px;border:1.5px solid var(--white);border-radius:50%}
.social.first{border-color:var(--amber)}
</style>
</head>
<body>

<!-- Hero -->
<div class="abs hero-photo" role="img" aria-label="Dark labyrinth of stone blocks seen from below"></div>
<svg class="abs hero-chevron" viewBox="0 0 1200 245" aria-hidden="true">
  <polygon points="0,27 600,190 1200,27 1200,245 0,245" fill="#000"/>
  <polyline points="0,27 600,190 1200,27" fill="none" stroke="var(--amber)" stroke-width="3"/>
</svg>

<nav class="nav">
  <a class="active" style="left:218px">ABOUT</a>
  <span class="sep" style="left:310px"></span>
  <a style="left:347px">GAMES</a>
  <a style="left:773px">CONTACT US</a>
  <span class="sep" style="left:913px"></span>
  <a style="left:952px">FAQ</a>
</nav>
<div class="abs brand"><div class="dot"></div><span>HOLLOW KEY</span></div>

<svg class="abs arrow-l" viewBox="0 0 36 36" aria-hidden="true"><polyline points="24,4 10,18 24,32" fill="none" stroke="#fff" stroke-width="4"/></svg>
<svg class="abs arrow-r" viewBox="0 0 36 36" aria-hidden="true"><polyline points="12,4 26,18 12,32" fill="none" stroke="#fff" stroke-width="4"/></svg>

<div class="abs center hero-kicker">WELCOME TO</div>
<h1 class="abs center hero-title">HOLLOW KEY</h1>
<div class="abs btn-book">BOOK NOW</div>

<!-- About -->
<div class="abs about-band"></div>
<svg class="abs about-hex" viewBox="0 0 360 412" role="img" aria-label="Person walking through a keyhole-shaped doorway into a starry nebula">
  <defs>
    <radialGradient id="nebula" cx="50%" cy="40%" r="60%">
      <stop offset="0" stop-color="#c2522a"/><stop offset=".45" stop-color="#5a1f1a"/><stop offset="1" stop-color="#141010"/>
    </radialGradient>
  </defs>
  <polygon points="180,2 358,104 358,308 180,410 2,308 2,104" fill="url(#nebula)" stroke="var(--amber)" stroke-width="1.5"/>
</svg>
<h2 class="abs about-title">WHAT AN ESCAPE ROOM</h2>
<p class="abs about-copy" style="top:936px">Fusce tellus Sed metus augue convallis et vehicula ut pulvinar eu ante Integer orci tellus tristique vitae consequat nec porta vel lectus Nulla sit amet daliquam enim Proin dui lectus</p>
<p class="abs about-copy" style="top:1038px">Aursus eu mattis laoreet viverra sit amet quam Curabitur vel dolor ultrices ipsum dictum tristique Praesent vitae lacus Ut velit enim vestibulum non fermentum nec hendrerit quis leo Pellentesque rutrum malesuada neque Nunc tempus felis vitae urna</p>
<div class="abs btn-outline btn-learn">LEARN MORE</div>

<!-- Who can play -->
<svg class="abs play-band" viewBox="0 0 1200 460" aria-hidden="true">
  <defs><linearGradient id="playGrad" x1="0" y1="0" x2="0" y2="1">
    <stop offset="0" stop-color="var(--brown)"/><stop offset="1" stop-color="var(--coal-2)"/></linearGradient></defs>
  <polygon points="0,72 606,7 1200,72 1200,460 0,460" fill="url(#playGrad)"/>
</svg>
<h2 class="abs center play-title">WHO CAN PLAY</h2>

<div class="abs player" style="left:139px">
  <svg width="92" height="104" viewBox="0 0 92 104" aria-hidden="true">
    <polygon points="46,2 90,27 90,77 46,102 2,77 2,27" fill="none" stroke="var(--amber)" stroke-width="1.5"/>
    <g fill="none" stroke="var(--amber)" stroke-width="2"><circle cx="36" cy="42" r="7"/><circle cx="58" cy="42" r="7"/><circle cx="47" cy="58" r="5"/><path d="M24 72c0-10 6-16 12-16s10 4 11 8M68 72c0-10-4-16-10-16"/></g>
  </svg>
  <h3>FAMILY</h3><p>Arerit quis leo Pellentesque rutrum malesuada neque Nunc tempus</p>
</div>
<div class="abs player" style="left:490px">
  <svg width="92" height="104" viewBox="0 0 92 104" aria-hidden="true">
    <polygon points="46,2 90,27 90,77 46,102 2,77 2,27" fill="none" stroke="var(--amber)" stroke-width="1.5"/>
    <g fill="none" stroke="var(--amber)" stroke-width="2"><circle cx="34" cy="38" r="6"/><circle cx="58" cy="38" r="6"/><circle cx="46" cy="56" r="6"/><path d="M24 54c0-6 4-9 10-9s10 3 10 9M48 54c0-6 4-9 10-9s10 3 10 9M34 74c0-8 5-11 12-11s12 3 12 11"/></g>
  </svg>
  <h3>CORPORATE</h3><p>Arerit quis leo Pellentesque rutrum malesuada neque Nunc tempus</p>
</div>
<div class="abs player" style="left:823px">
  <svg width="92" height="104" viewBox="0 0 92 104" aria-hidden="true">
    <polygon points="46,2 90,27 90,77 46,102 2,77 2,27" fill="none" stroke="var(--amber)" stroke-width="1.5"/>
    <g fill="none" stroke="var(--amber)" stroke-width="2"><circle cx="32" cy="40" r="6"/><circle cx="46" cy="36" r="6"/><circle cx="60" cy="40" r="6"/><path d="M22 74V56c0-5 4-8 10-8s10 3 10 8v18M36 74V52c0-5 4-8 10-8s10 3 10 8v22M50 74V56c0-5 4-8 10-8s10 3 10 8v18"/></g>
  </svg>
  <h3>FRIENDS</h3><p>Arerit quis leo Pellentesque rutrum malesuada neque Nunc tempus</p>
</div>

<!-- How it works -->
<div class="abs how-photo" role="img" aria-label="Dim stone brick corridor"></div>
<svg class="abs how-chevron" viewBox="0 0 1200 125" aria-hidden="true">
  <polygon points="0,0 1200,0 1200,14 606,115 0,14" fill="var(--coal-2)"/>
  <polyline points="0,14 606,115 1200,14" fill="none" stroke="var(--amber)" stroke-width="2.5"/>
</svg>
<h2 class="abs center how-title">HOW IT WORKS</h2>
<p class="abs center how-copy">Fusce tellus Sed metus augue convallis et vehicula ut pulvinar eu ante Integer orci tellus tristique<br>vitae consequat nec porta vel lectus Nulla sit amet daliquam enim</p>

<div class="abs step" style="left:134px">
  <svg class="ring" viewBox="0 0 142 142" aria-hidden="true">
    <circle cx="71" cy="71" r="69" fill="none" stroke="var(--amber)" stroke-width="2.5"/>
    <g fill="none" stroke="var(--amber)" stroke-width="2.5"><circle cx="50" cy="58" r="7"/><circle cx="71" cy="52" r="8"/><circle cx="92" cy="58" r="7"/><path d="M36 90c0-12 6-19 14-19M106 90c0-12-6-19-14-19M54 92c0-14 8-21 17-21s17 7 17 21z"/></g>
  </svg>
  <h3>2 TO 6 PLAYERS</h3><p>Apulvinar eu ante Integer orci tellus<br>tristique vitae consequat nec</p>
</div>
<svg class="abs step-arrow" style="left:410px" viewBox="0 0 70 50" aria-hidden="true"><path d="M4 8c20 0 40 14 60 30M50 40l14-2-4-14" fill="none" stroke="var(--amber-soft)" stroke-width="2"/></svg>
<div class="abs step" style="left:450px">
  <svg class="ring" viewBox="0 0 142 142" aria-hidden="true">
    <circle cx="71" cy="71" r="69" fill="none" stroke="var(--amber)" stroke-width="2.5"/>
    <g fill="none" stroke="var(--amber)" stroke-width="2.5"><circle cx="71" cy="34" r="7"/><path d="M71 41v22M71 50h6M71 57h6"/><circle cx="56" cy="80" r="9"/><path d="M50 87l-16 16M40 97l5 5"/><circle cx="86" cy="80" r="9"/><path d="M92 87l14 14M100 95l-4 4"/></g>
  </svg>
  <h3>60 MINUTES OF GAME</h3><p>Apulvinar eu ante Integer orci tellus<br>tristique vitae consequat nec</p>
</div>
<svg class="abs step-arrow" style="left:720px" viewBox="0 0 70 50" aria-hidden="true"><path d="M4 44c16-20 36-32 60-32M50 4l14 8-10 12" fill="none" stroke="var(--amber-soft)" stroke-width="2"/></svg>
<div class="abs step" style="left:766px">
  <svg class="ring" viewBox="0 0 142 142" role="img" aria-label="Dragon head illustration">
    <circle cx="71" cy="71" r="69" fill="none" stroke="var(--amber)" stroke-width="2.5"/>
  </svg>
  <h3>TONS OF ADVENTURE</h3><p>Apulvinar eu ante Integer orci tellus<br>tristique vitae consequat nec</p>
</div>

<!-- Booking -->
<div class="abs book-band"></div>
<h2 class="abs center book-title">BOOK APPOINTMENT</h2>
<p class="abs center book-copy">Fusce tellus Sed metus augue convallis et vehicula ut pulvinar eu ante Integer orci tellus tristique<br>vitae consequat nec porta vel lectus Nulla sit amet daliquam enim</p>
<div class="abs btn-schedule">SCHEDULING OF APPOINTMENTS</div>

<svg class="abs foot-chevron" viewBox="0 0 1200 267" aria-hidden="true">
  <polygon points="0,105 598,25 1200,105 1200,267 0,267" fill="#000"/>
  <polyline points="0,105 598,25 1200,105" fill="none" stroke="var(--amber)" stroke-width="2.5"/>
</svg>
<div class="abs foot-brand"><div class="dot"></div><span>HOLLOW KEY</span></div>

<!-- Footer -->
<nav class="foot-nav">
  <a style="left:347px">HOME</a>
  <a style="left:465px">ABOUT</a>
  <a style="left:587px">GAMES</a>
  <a style="left:735px">CONTACT US</a>
  <a style="left:877px">FAQ</a>
</nav>
<p class="abs center copyright">© 2020 Company Name | All Rights Reserved | Disclaimer</p>
<div class="abs social first" style="left:524px"></div>
<div class="abs social" style="left:563px"></div>
<div class="abs social" style="left:602px"></div>
<div class="abs social" style="left:641px"></div>

</body>
</html>
```